Business Card For Quillmoor Financial Consulting

Hi, I would like a business card designed. Bold, modern.
Please use the same design as the logo. I have also attached the website design to see the overall theme.
Wordmark Font
Color: Hex: #01AEF7

```html
<!DOCTYPE html>
<html lang="en">
<head>
<meta charset="utf-8">
<title>Quillmoor Consulting – Business Card</title>
<link href="https://fonts.googleapis.com/css2?family=Montserrat:wght@400;500;700&display=swap" rel="stylesheet">
<style>
  :root {
    --brand-blue: #01aef7;
    --brand-navy: #0d3a5c;
    --ink: #2a2d33;
    --paper: #ffffff;
    --paper-shade: #eceeef;
    --night: #0f1216;
    --night-soft: #1b2027;
    --stage: #3a3d42;
  }
  * { box-sizing: border-box; margin: 0; padding: 0; }
  html, body { width: 1200px; height: 960px; overflow: hidden; }
  body {
    background: var(--stage);
    font-family: "Montserrat", sans-serif;
    display: flex;
    flex-direction: column;
    align-items: center;
    justify-content: center;
    gap: 48px;
  }
  .card {
    position: relative;
    width: 700px;
    height: 400px;
    overflow: hidden;
    box-shadow: 0 14px 30px rgba(0,0,0,0.45);
  }

  /* Dark side */
  .card--back { background: linear-gradient(160deg, var(--night-soft), var(--night)); }
  .back-brand {
    position: absolute; left: 60px; top: 60px;
    display: flex; align-items: center; gap: 18px;
  }
  .brand-square {
    width: 56px; height: 56px;
    border: 4px solid var(--brand-blue);
  }
  .back-brand .brand-name {
    color: #ffffff; font-weight: 700; font-size: 38px; letter-spacing: 4px;
    text-transform: uppercase;
  }
  .back-visual {
    position: absolute; left: 220px; right: 0; bottom: 0; height: 220px;
    background:
      radial-gradient(ellipse at 60% 80%, rgba(1,174,247,0.55), rgba(1,174,247,0) 65%),
      linear-gradient(180deg, rgba(15,18,22,0), #0a2a44 85%);
  }

  /* Light side */
  .card--front { background: linear-gradient(135deg, var(--paper) 40%, var(--paper-shade)); }
  .front-square {
    position: absolute; left: 70px; top: 40px;
    width: 90px; height: 90px;
    border: 6px solid var(--brand-blue);
  }
  .holder {
    position: absolute; left: 70px; top: 150px;
  }
  .holder-name { color: var(--brand-blue); font-size: 30px; font-weight: 400; }
  .holder-role { color: var(--ink); font-size: 16px; margin-top: 2px; }
  .divider {
    position: absolute; left: 250px; right: 60px; top: 196px;
    height: 1px; background: var(--brand-blue);
  }
  .front-brand {
    position: absolute; right: 60px; top: 70px;
    color: var(--brand-navy); font-weight: 700; font-size: 26px; letter-spacing: 3px;
    text-transform: uppercase; text-align: right;
  }
  .address {
    position: absolute; left: 70px; top: 228px;
    color: var(--ink); font-size: 17px; line-height: 1.4;
  }
  .contacts {
    position: absolute; left: 70px; top: 290px;
    list-style: none; color: var(--ink); font-size: 17px; line-height: 1.55;
  }
  .contacts li { display: flex; align-items: center; gap: 12px; }
  .contacts svg { width: 16px; height: 16px; flex: none; }
  .web-accent { color: var(--brand-blue); }
</style>
</head>
<body>

  <section class="card card--back">
    <div class="back-brand">
      <div class="brand-square"></div>
      <span class="brand-name">Quillmoor Consulting</span>
    </div>
    <div class="back-visual" role="img" aria-label="Glowing blue three-dimensional rising bar chart"></div>
  </section>

  <section class="card card--front">
    <div class="front-square"></div>
    <div class="holder">
      <p class="holder-name">Mara Ellison</p>
      <p class="holder-role">Chairmen</p>
    </div>
    <div class="divider"></div>
    <p class="front-brand">Quillmoor Consulting</p>
    <p class="address">2178 Harlow Terrace Suite 14,<br>West Brennfield</p>
    <ul class="contacts">
      <li>
        <svg viewBox="0 0 16 16" aria-hidden="true"><path fill="#01aef7" d="M3.5 1.5l2.5 0 1 3.5-1.6 1.2a8 8 0 0 0 4.4 4.4L11 9l3.5 1v2.5c0 1-1 2-2 2C6.5 14.5 1.5 9.5 1.5 3.5c0-1 1-2 2-2z"/></svg>
        +1 555 014 2290
      </li>
      <li>
        <svg viewBox="0 0 16 16" aria-hidden="true"><rect x="1" y="3" width="14" height="10" fill="#01aef7"/><path d="M1 3l7 6 7-6" fill="none" stroke="#fff" stroke-width="1.4"/></svg>
        hello@quillmoorfinancial.com
      </li>
      <li>
        <svg viewBox="0 0 16 16" aria-hidden="true"><circle cx="8" cy="8" r="7" fill="#01aef7"/><path d="M1 8h14M8 1c-3 3.5-3 10.5 0 14M8 1c3 3.5 3 10.5 0 14" fill="none" stroke="#fff" stroke-width="1"/></svg>
        <span>www.<span class="web-accent">quillmoorfinancial</span>.com</span>
      </li>
    </ul>
  </section>

</body>
</html>
```